Business Card/Logo Design Project

Design the Business card For a psychologist providing relationship workshops, see website draft at www.quietbridgeworks.com.au.

The background is to be beige with shadows in ivory of the letter "L" as shown on the website noted above.

The words "Kind Harbour" on the front with the first letter of each word in very scrolled lettering and the remaining letters more formal. The front design is to be the logo of the business for use on other items.

The reverse is to show...

client's name
date
time
workshop number
workshop name
and at the bottom "PLEASE BE PUNCTUAL. BRING NOTEPAD & PEN"

Target Market(s)

female, middle-class, educated, introspective

Industry/Entity Type

Business

Requirements
Must have
• see www.quietbridgeworks.com.au for the design aesthetic - just need you to make it look professional.

cream, beige, grey, chocolate, tan, ivory.

calligraphy shadows as per referenced website

business card back, flyer and postcard to just be background so that I can add text on top through printmarlow.

see website for colour-scheme.
Should not have
• not cutesy, pink, or mushy

```html
<!DOCTYPE html>
<html lang="en">
<head>
<meta charset="utf-8">
<title>Kind Harbour – Business Card</title>
<link href="https://fonts.googleapis.com/css2?family=Libre+Baskerville:wght@400;700&display=swap" rel="stylesheet">
<style>
  :root {
    --page: #ffffff;
    --card: #cdb3a8;
    --card-light: #d8c2b8;
    --ivory: #efe3dc;
    --chocolate: #6b2a10;
    --rule: #e6d6ce;
  }
  * { margin: 0; padding: 0; box-sizing: border-box; }
  html, body {
    width: 1200px;
    height: 1200px;
    overflow: hidden;
    background: var(--page);
  }
  body {
    position: relative;
    font-family: "Libre Baskerville", Georgia, serif;
  }
  .card {
    position: absolute;
    left: 152px;
    background: var(--card);
    overflow: hidden;
  }
  .card--front { top: 56px; width: 868px; height: 504px; }
  .card--back  { top: 632px; width: 870px; height: 508px; }

  .flourish-backdrop {
    position: absolute;
    inset: 0;
    background:
      radial-gradient(ellipse at 22% 38%, var(--card-light) 0%, rgba(216,194,184,0) 55%),
      radial-gradient(ellipse at 85% 95%, var(--card-light) 0%, rgba(216,194,184,0) 45%),
      linear-gradient(135deg, #d3bbb0 0%, var(--card) 60%, #c9ada1 100%);
  }
  .brand {
    position: absolute;
    right: 14px;
    top: 282px;
    text-align: right;
    color: var(--chocolate);
    font-weight: 400;
  }
  .brand__name {
    font-size: 54px;
    line-height: 1;
    letter-spacing: 0.5px;
  }
  .brand__suffix {
    font-size: 19px;
    line-height: 1.2;
    margin-top: 2px;
  }

  .back__title {
    position: absolute;
    top: 16px;
    left: 0;
    right: 0;
    text-align: center;
    font-weight: 700;
    font-size: 40px;
    color: var(--chocolate);
  }
  .field {
    position: absolute;
    left: 28px;
    right: 24px;
    display: flex;
    align-items: baseline;
    font-weight: 700;
    font-size: 31px;
    color: var(--ivory);
    white-space: nowrap;
  }
  .field__line {
    flex: 1;
    border-bottom: 1px solid var(--rule);
    margin-left: 4px;
    transform: translateY(-4px);
  }
  .field--client { top: 112px; }
  .field--date { top: 210px; }
  .field--date .field__line--date { flex: 0 0 450px; margin-right: 2px; }
  .field--workshop { top: 306px; }
  .rule-extra {
    position: absolute;
    left: 28px;
    right: 24px;
    top: 408px;
    border-bottom: 1px solid var(--rule);
  }
  .back__note {
    position: absolute;
    bottom: 16px;
    left: 0;
    right: 0;
    text-align: center;
    font-weight: 700;
    font-size: 32px;
    color: var(--chocolate);
  }
</style>
</head>
<body>
  <section class="card card--front">
    <div class="flourish-backdrop" role="img" aria-label="Large ivory calligraphic letter flourishes with soft shadows across a beige background"></div>
    <div class="brand">
      <div class="brand__name">Kind Harbour</div>
      <div class="brand__suffix">.com.au</div>
    </div>
  </section>

  <section class="card card--back">
    <h1 class="back__title">Appointment/ Workshop</h1>
    <div class="field field--client"><span>Client Name</span><span class="field__line"></span></div>
    <div class="field field--date"><span>Date(s)</span><span class="field__line field__line--date"></span><span>Time</span><span class="field__line"></span></div>
    <div class="field field--workshop"><span>Workshop No’ &amp; Name</span><span class="field__line"></span></div>
    <div class="rule-extra"></div>
    <p class="back__note">Please be Punctual. Bring a Notepad &amp; Pen.</p>
  </section>
</body>
</html>
```